Redesign cement bags for leading cement producer in south east asia

We are from Larkfield cement and would like to redesign our bag to relaunch the product line. Our bags are made of high quality PP woven sack. We are one of the leading cement producers and we want our bags to have a Larkfield classy look on each visible side when it is loading in a truck or stacking on a pallet.

Thank you for interesting in this project. Good luck.

Project Deadline Extended Reason: Hi all, I have received requests to extend the deadline. Some of the work requires revising and some of them are still on process. To be fair, I also raise my budget to compensate the time. Thanks all for your participation. Added Sunday, July 10, 2016

Target Market(s)

Construction

Industry/Entity Type

Cement

Requirements
Must have
• You will have to design two bags for two cement grades. 52.5 is of higher grade and 42.5 is of lower grade. Both are similar in design but a distinctive colours to differentiate the two at once. Please look at Reference picture 2 for ideas.
Nice to have
• You do not have to change the original logo but the Larkfield cement word font changes are required. There are no restrictions to colours and font but please refrain from using feminine colours. Instructions on rear side of the bags are now included in the scope. Please create new layout and design new user friendly symbols.
Should not have
• Since cement is a dusty product, you need avoid some colours like black as background. The dust need to be less obvious to attract attention. Our previous base colour are shown in below.
• We want a fresh look on our bag, please do not just copy our old design and make small changes. I have attached our competitors' design, please refrain from using their design as well.
• It is recommend to do some research on cement bag sector.

```html
<!DOCTYPE html>
<html lang="en">
<head>
<meta charset="utf-8">
<title>Larkfield Cement 42.5 Bag</title>
<link rel="stylesheet" href="https://fonts.googleapis.com/css2?family=Roboto:wght@400;700;900&display=swap">
<style>
  :root {
    --bag-white: #f1f1f1;
    --bag-grey: #e4e4e4;
    --side-white: #e9e9e9;
    --bag-blue: #2294cf;
    --side-blue: #1f86bd;
    --bag-blue-deep: #1c72a6;
    --grade-blue: #87c0df;
    --grade-grey: #8a8a8a;
    --ink: #262626;
    --paper: #ffffff;
  }
  * { margin: 0; padding: 0; box-sizing: border-box; }
  html, body { width: 1200px; height: 1200px; overflow: hidden; background: var(--paper); }
  body { font-family: "Roboto", Arial, sans-serif; color: var(--ink); }
  .canvas { position: relative; width: 1200px; height: 1200px; }

  /* top gusset */
  .bag-top {
    position: absolute; left: 235px; top: 120px; width: 730px; height: 140px;
    background: var(--bag-grey);
  }
  .top-info {
    position: absolute; left: 60px; top: 26px; width: 230px;
    transform: rotate(180deg); text-align: center;
    font-size: 12px; line-height: 14.5px; font-weight: 400;
  }
  .top-info .caps { font-size: 13px; }
  .top-brand {
    position: absolute; left: 400px; top: 30px; width: 180px;
    transform: rotate(180deg);
    display: flex; flex-direction: column; align-items: center; line-height: 1;
  }
  .top-brand .brand-name { font-size: 22px; font-weight: 900; }
  .top-brand .brand-mark { width: 26px; height: 26px; border-radius: 50%; background: var(--bag-blue); margin: 8px 0; }
  .top-brand .brand-word { font-size: 15px; font-weight: 900; }

  /* front face */
  .bag-front {
    position: absolute; left: 235px; top: 260px;
    width: 560px; height: 820px; overflow: hidden;
    background: var(--bag-white);
  }
  .bag-front svg, .bag-side svg { position: absolute; inset: 0; }
  .brand { position: absolute; width: 300px; text-align: center; line-height: 1; }
  .brand-name { font-weight: 900; }
  .brand-word { font-weight: 700; }
  .front-name-top { left: 5px; top: 31px; font-size: 52px; }
  .front-mark-top { position: absolute; left: 105px; top: 105px; width: 100px; height: 100px; border-radius: 50%; background: var(--bag-blue); }
  .front-word-top { left: 5px; top: 238px; font-size: 44px; }
  .grade {
    position: absolute; left: 0; width: 560px; top: 341px;
    text-align: center; color: var(--grade-blue);
    font-size: 215px; font-weight: 700; letter-spacing: -3px; line-height: 1;
  }
  .front-name-bottom { left: 130px; top: 542px; font-size: 44px; }
  .front-mark-bottom { position: absolute; left: 236px; top: 603px; width: 88px; height: 88px; border-radius: 50%; background: var(--paper); }
  .front-word-bottom { left: 130px; top: 715px; font-size: 44px; }
  .net-weight {
    position: absolute; left: 130px; width: 300px; top: 764px;
    text-align: center; color: var(--paper); font-weight: 700; font-size: 21px; line-height: 1.05;
  }

  /* side gusset */
  .bag-side {
    position: absolute; left: 795px; top: 260px; width: 170px; height: 820px;
    overflow: hidden; background: var(--side-white);
  }
  .side-block {
    position: absolute; writing-mode: vertical-rl; transform: rotate(180deg);
    display: flex; flex-direction: column; line-height: 1.05;
  }
  .side-spec { left: 14px; top: 14px; height: 206px; align-items: flex-start; gap: 6px; }
  .side-spec .side-grade { font-size: 64px; font-weight: 700; color: var(--grade-grey); letter-spacing: -1px; line-height: 1; }
  .side-spec .side-line { font-size: 17px; }
  .side-spec .side-small { font-size: 12.5px; }
  .side-origin { left: 40px; top: 285px; height: 215px; align-items: flex-start; color: var(--ink); }
  .side-origin .side-line { font-size: 17px; }
  .side-origin .side-small { font-size: 13px; }
  .side-brand { left: 40px; top: 590px; height: 190px; align-items: center; gap: 8px; line-height: 1; }
  .side-brand .brand-name { font-size: 26px; }
  .side-brand .brand-mark { width: 28px; height: 28px; border-radius: 50%; background: var(--paper); }
  .side-brand .brand-word { font-size: 22px; }
</style>
</head>
<body>
<div class="canvas">

  <div class="bag-top">
    <div class="top-info">
      <p class="caps">EXPORT QUALITY</p>
      <p class="caps">PRODUCT OF MYANMAR</p>
      <p>Portland Cement</p>
      <p>EN 197-1 (2000), Strength Class 42.5</p>
      <p>Net Weight</p>
      <p>50 Kg</p>
    </div>
    <div class="top-brand">
      <span class="brand-name">LARKFIELD</span>
      <span class="brand-mark"></span>
      <span class="brand-word">CEMENT</span>
    </div>
  </div>

  <div class="bag-front">
    <svg width="560" height="820" viewBox="0 0 560 820" aria-hidden="true">
      <path d="M0,310 C120,382 260,372 380,320 S520,245 560,238 L560,820 L0,820 Z" fill="var(--bag-blue-deep)"/>
      <path d="M0,322 C120,396 260,386 380,336 S520,262 560,256 L560,820 L0,820 Z" fill="var(--bag-blue)"/>
    </svg>
    <div class="brand brand-name front-name-top">LARKFIELD</div>
    <span class="front-mark-top"></span>
    <div class="brand brand-word front-word-top">CEMENT</div>
    <div class="grade">42.5</div>
    <div class="brand brand-name front-name-bottom">LARKFIELD</div>
    <span class="front-mark-bottom"></span>
    <div class="brand brand-word front-word-bottom">CEMENT</div>
    <div class="net-weight">Net Weight<br>50 Kg</div>
  </div>

  <div class="bag-side">
    <svg width="170" height="820" viewBox="0 0 170 820" aria-hidden="true">
      <path d="M0,238 C60,232 120,226 170,220 L170,820 L0,820 Z" fill="var(--bag-blue-deep)"/>
      <path d="M0,256 C60,250 120,244 170,238 L170,820 L0,820 Z" fill="var(--side-blue)"/>
    </svg>
    <div class="side-block side-spec">
      <span class="side-grade">42.5</span>
      <span class="side-line">Portland Cement</span>
      <span class="side-small">EN 197-1 (2000), Strength Class 42.5</span>
    </div>
    <div class="side-block side-origin">
      <span class="side-line">EXPORT QUALITY</span>
      <span class="side-line">PRODUCT OF MYANMAR</span>
      <span class="side-small">Net Weight</span>
      <span class="side-small">50 Kg</span>
    </div>
    <div class="side-block side-brand">
      <span class="brand-name">LARKFIELD</span>
      <span class="brand-mark"></span>
      <span class="brand-word">CEMENT</span>
    </div>
  </div>

</div>
</body>
</html>
```